Core Values Poster for Healthcare company

Trying to Create a core values poster for my company. Healthcare Company - We have Neurosurgery, Pain Management, Physical Therapy, Occupational Therapy, Rehab, Imaging, and psychology so far and we are growing fast.

Core Values would Include - (Execution), (Loyalty), (Innovation), (Synergy), (Growth-Oriented), (Ethics & Integrity), (Love), and (Energy)

Please incorporate the Company Logo which is on the website and I have included it in my uploads. As long as the logo stays blue it does not need a gradient effect.

I like the posters made for this contest : https://quillvane.com.au/poster-design/contests/make-team-principles-wallchart-815327

This picture should be memorable so people know our Core Values

Target Market(s)

Staff in the company

Colors

Designer to choose colors to be used in the design.

Requirements
Must have
• Logo
Nice to have
• Pictures for each core value

```html
<!DOCTYPE html>
<html lang="en">
<head>
<meta charset="utf-8">
<title>Core Values — Lumencare</title>
<link rel="stylesheet" href="https://fonts.googleapis.com/css2?family=Montserrat:wght@500;600&display=swap">
<style>
  :root {
    --bg-top: #eef0f1;
    --bg-bottom: #cfd3d5;
    --band: #1f9fb5;
    --band-dark: #137e92;
    --ink: #124a5c;
    --execution: #0f4f63;
    --loyalty: #1b9bb0;
    --innovation: #e98a1c;
    --synergy: #5aa52d;
    --growth: #e0561c;
    --ethics: #a3a3a3;
    --love: #25abc2;
    --energy: #eaa020;
    --side-blue: #afd3dc;
    --side-tan: #d6b48c;
    --edge: #f7f8f8;
    --hub: #e4e8ea;
  }
  * { margin: 0; padding: 0; box-sizing: border-box; }
  html, body { width: 1200px; height: 1148px; overflow: hidden; }
  body {
    background: linear-gradient(180deg, var(--bg-top) 0%, var(--bg-bottom) 100%);
    font-family: "Montserrat", sans-serif;
    position: relative;
  }
  .poster-title {
    position: absolute; top: 100px; left: 40px; right: 40px;
    display: flex; align-items: center; gap: 18px;
  }
  .poster-title .band { flex: 1; height: 16px; background: linear-gradient(90deg, var(--band), var(--band-dark)); }
  .poster-title h1 {
    font-size: 30px; font-weight: 600; color: var(--ink); letter-spacing: 1px;
  }
  .values-wheel { position: absolute; left: 0; top: 180px; }
  .value-label { font-family: "Montserrat", sans-serif; font-weight: 500; font-size: 17px; fill: #fff; letter-spacing: 1px; }
  .hub-name { font-family: "Montserrat", sans-serif; font-weight: 600; font-size: 24px; fill: var(--ink); letter-spacing: 2px; }
  .brand-lockup {
    position: absolute; top: 965px; left: 0; right: 0;
    display: flex; justify-content: center; align-items: center;
  }
  .brand-name {
    font-family: "Montserrat", sans-serif; font-weight: 600; font-size: 58px;
    color: var(--ink); letter-spacing: 6px; line-height: 1;
  }
</style>
</head>
<body>
  <header class="poster-title">
    <span class="band"></span>
    <h1>CORE VALUES</h1>
    <span class="band"></span>
  </header>

  <svg class="values-wheel" width="1200" height="760" viewBox="0 0 1200 760" aria-label="Eight core values arranged around the company name">
    <defs>
      <filter id="lift" x="-20%" y="-20%" width="140%" height="140%">
        <feDropShadow dx="3" dy="5" stdDeviation="5" flood-color="#000" flood-opacity="0.22"/>
      </filter>
      <g id="side-piece-shape">
        <path d="M30 110 L220 150 A38 38 0 1 1 290 165 L370 185 L370 560 L240 600 A38 38 0 1 0 170 620 L30 660 Z" fill="var(--edge)"/>
      </g>
    </defs>

    <g class="side-piece side-piece--left" filter="url(#lift)">
      <use href="#side-piece-shape"/>
      <path d="M50 140 L350 205 L350 545 L250 575 A45 45 0 0 0 165 600 L50 630 Z" fill="var(--side-blue)"/>
    </g>
    <g class="side-piece side-piece--right" filter="url(#lift)" transform="translate(1200 0) scale(-1 1)">
      <use href="#side-piece-shape"/>
      <path d="M50 140 L350 205 L350 545 L250 575 A45 45 0 0 0 165 600 L50 630 Z" fill="var(--side-tan)"/>
    </g>

    <g transform="translate(600 380)">
      <g class="hub">
        <circle r="130" fill="var(--hub)" filter="url(#lift)"/>
        <text class="hub-name" x="0" y="9" text-anchor="middle">LUMENCARE</text>
      </g>

      <g class="value value--execution" filter="url(#lift)">
        <path d="M-124 -296 L124 -296 L60 -144 L-60 -144 Z" fill="var(--edge)"/>
        <path d="M-110 -286 L110 -286 L54 -154 L-54 -154 Z" fill="var(--execution)"/>
        <circle cx="88" cy="-220" r="14" fill="var(--edge)"/>
        <text class="value-label" x="0" y="-258" text-anchor="middle">EXECUTION</text>
        <g transform="translate(0 -205)" fill="none" stroke="#fff" stroke-width="3">
          <rect x="-16" y="-20" width="32" height="40" rx="3"/>
          <path d="M-9 0 L-2 8 L11 -9"/>
        </g>
      </g>
      <g class="value value--loyalty" transform="rotate(45)" filter="url(#lift)">
        <path d="M-124 -296 L124 -296 L60 -144 L-60 -144 Z" fill="var(--edge)"/>
        <path d="M-110 -286 L110 -286 L54 -154 L-54 -154 Z" fill="var(--loyalty)"/>
        <circle cx="88" cy="-220" r="14" fill="var(--edge)"/>
        <text class="value-label" x="0" y="-258" text-anchor="middle">LOYALTY</text>
        <g transform="translate(0 -205) rotate(-45)" fill="none" stroke="#fff" stroke-width="3">
          <path d="M-20 -4 L-8 -14 L4 -6 L14 -14 L22 -4 L8 10 L-6 12 Z"/>
        </g>
      </g>
      <g class="value value--innovation" transform="rotate(90)" filter="url(#lift)">
        <path d="M-124 -296 L124 -296 L60 -144 L-60 -144 Z" fill="var(--edge)"/>
        <path d="M-110 -286 L110 -286 L54 -154 L-54 -154 Z" fill="var(--innovation)"/>
        <circle cx="88" cy="-220" r="14" fill="var(--edge)"/>
        <text class="value-label" x="0" y="-258" text-anchor="middle">INNOVATION</text>
        <g transform="translate(0 -205) rotate(-90)" fill="none" stroke="#fff" stroke-width="3">
          <circle cx="0" cy="-6" r="12"/>
          <path d="M-6 8 L6 8 M-5 14 L5 14"/>
        </g>
      </g>
      <g class="value value--synergy" transform="rotate(135)" filter="url(#lift)">
        <path d="M-124 -296 L124 -296 L60 -144 L-60 -144 Z" fill="var(--edge)"/>
        <path d="M-110 -286 L110 -286 L54 -154 L-54 -154 Z" fill="var(--synergy)"/>
        <circle cx="88" cy="-220" r="14" fill="var(--edge)"/>
        <text class="value-label" x="0" y="-258" text-anchor="middle" transform="rotate(180 0 -263)">SYNERGY</text>
        <g transform="translate(0 -205)" fill="#fff">
          <circle cx="0" cy="-12" r="7"/><circle cx="-12" cy="8" r="7"/><circle cx="12" cy="8" r="7"/>
        </g>
      </g>
      <g class="value value--growth" transform="rotate(180)" filter="url(#lift)">
        <path d="M-124 -296 L124 -296 L60 -144 L-60 -144 Z" fill="var(--edge)"/>
        <path d="M-110 -286 L110 -286 L54 -154 L-54 -154 Z" fill="var(--growth)"/>
        <circle cx="88" cy="-220" r="14" fill="var(--edge)"/>
        <g transform="rotate(180 0 -250)">
          <text class="value-label" x="0" y="-244" text-anchor="middle">GROWTH-</text>
          <text class="value-label" x="0" y="-224" text-anchor="middle">ORIENTED</text>
        </g>
        <g transform="translate(0 -190) rotate(180)" fill="#fff">
          <rect x="-16" y="4" width="6" height="10"/><rect x="-6" y="-2" width="6" height="16"/><rect x="4" y="-8" width="6" height="22"/>
          <path d="M-18 -2 L0 -14 L12 -22" fill="none" stroke="#fff" stroke-width="3"/>
        </g>
      </g>
      <g class="value value--ethics" transform="rotate(225)" filter="url(#lift)">
        <path d="M-124 -296 L124 -296 L60 -144 L-60 -144 Z" fill="var(--edge)"/>
        <path d="M-110 -286 L110 -286 L54 -154 L-54 -154 Z" fill="var(--ethics)"/>
        <circle cx="88" cy="-220" r="14" fill="var(--edge)"/>
        <g transform="rotate(180 0 -258)">
          <text class="value-label" x="0" y="-262" text-anchor="middle">ETHICS &amp;</text>
          <text class="value-label" x="0" y="-242" text-anchor="middle">INTEGRITY</text>
        </g>
        <g transform="translate(0 -195) rotate(135)" fill="none" stroke="#fff" stroke-width="3">
          <rect x="-14" y="-16" width="22" height="28" rx="2"/><rect x="-6" y="-8" width="22" height="28" rx="2"/>
        </g>
      </g>
      <g class="value value--love" transform="rotate(270)" filter="url(#lift)">
        <path d="M-124 -296 L124 -296 L60 -144 L-60 -144 Z" fill="var(--edge)"/>
        <path d="M-110 -286 L110 -286 L54 -154 L-54 -154 Z" fill="var(--love)"/>
        <circle cx="88" cy="-220" r="14" fill="var(--edge)"/>
        <text class="value-label" x="0" y="-258" text-anchor="middle">LOVE</text>
        <g transform="translate(0 -205) rotate(90)">
          <path d="M0 14 L-16 -2 A9 9 0 0 1 0 -12 A9 9 0 0 1 16 -2 Z" fill="none" stroke="#fff" stroke-width="3"/>
        </g>
      </g>
      <g class="value value--energy" transform="rotate(315)" filter="url(#lift)">
        <path d="M-124 -296 L124 -296 L60 -144 L-60 -144 Z" fill="var(--edge)"/>
        <path d="M-110 -286 L110 -286 L54 -154 L-54 -154 Z" fill="var(--energy)"/>
        <circle cx="88" cy="-220" r="14" fill="var(--edge)"/>
        <text class="value-label" x="0" y="-258" text-anchor="middle">ENERGY</text>
        <g transform="translate(0 -205) rotate(45)">
          <circle r="20" fill="none" stroke="#fff" stroke-width="3"/>
          <path d="M3 -13 L-7 2 L0 2 L-3 13 L7 -2 L0 -2 Z" fill="#fff"/>
        </g>
      </g>
    </g>
  </svg>

  <footer class="brand-lockup">
    <span class="brand-name">LUMENCARE</span>
  </footer>
</body>
</html>
```